Business cards and stationery for a software company
Klovarent s.r.o.
Simple
Petr Hrubeš
Lipová alej 2841/9
Praha 5
petr.hrubes@klovarent-example.com
www.klovarent-example.com

```html
<!DOCTYPE html>
<html lang="cs">
<head>
<meta charset="utf-8">
<title>Klovarent s.r.o. – vizitka</title>
<link rel="stylesheet" href="https://fonts.googleapis.com/css2?family=Montserrat:wght@700&family=Open+Sans:ital,wght@0,400;0,600;1,600&display=swap">
<style>
  :root {
    --backdrop: #e9e7e4;
    --card: #ffffff;
    --ink: #3a3a3c;
    --muted: #7a7a7e;
    --brand: #7b3fa0;
    --brand-dark: #5e2c80;
    --rule: #d6d3d8;
    --band-text: #e6d6f0;
  }
  * { box-sizing: border-box; margin: 0; padding: 0; }
  html, body { width: 1200px; height: 629px; overflow: hidden; }
  body {
    background: var(--backdrop);
    font-family: "Open Sans", Arial, sans-serif;
    color: var(--ink);
    display: flex;
    align-items: center;
    justify-content: center;
    gap: 60px;
  }
  .card {
    width: 520px;
    height: 297px;
    background: var(--card);
    position: relative;
    box-shadow: 0 6px 20px rgba(0,0,0,.12);
    overflow: hidden;
  }
  .wordmark {
    display: flex;
    align-items: center;
    gap: 10px;
    font-family: "Montserrat", Arial, sans-serif;
    font-weight: 700;
    color: var(--brand);
    letter-spacing: -0.5px;
  }
  .wordmark .dot {
    border-radius: 50%;
    background: var(--brand);
  }
  .card-front {
    display: flex;
    align-items: center;
    justify-content: center;
  }
  .card-front .wordmark { font-size: 40px; }
  .card-front .wordmark .dot { width: 34px; height: 34px; }

  .card-back .wordmark {
    position: absolute;
    left: 60px;
    top: 62px;
    font-size: 30px;
  }
  .card-back .wordmark .dot { width: 26px; height: 26px; }

  .holder {
    position: absolute;
    left: 40px;
    top: 130px;
    width: 170px;
    text-align: right;
    font-size: 10px;
    line-height: 1.6;
    color: var(--muted);
  }
  .holder .name {
    font-style: italic;
    font-weight: 600;
    font-size: 12px;
    color: var(--ink);
    margin-bottom: 6px;
  }
  .divider {
    position: absolute;
    left: 232px;
    top: 120px;
    width: 1px;
    height: 110px;
    background: var(--rule);
  }
  .contacts {
    position: absolute;
    left: 250px;
    top: 128px;
    list-style: none;
    font-size: 10px;
    color: var(--muted);
  }
  .contacts li {
    display: flex;
    align-items: center;
    gap: 8px;
    height: 24px;
  }
  .contacts svg { width: 15px; height: 15px; flex: none; }
  .band {
    position: absolute;
    left: 0; right: 0; bottom: 0;
    height: 34px;
    background: linear-gradient(90deg, var(--brand-dark), var(--brand));
    display: flex;
    align-items: center;
    justify-content: center;
    color: var(--band-text);
    font-size: 9px;
    letter-spacing: 4px;
  }
</style>
</head>
<body>
  <section class="card card-front" aria-label="Přední strana vizitky">
    <div class="wordmark"><span class="dot"></span>Klovarent</div>
  </section>

  <section class="card card-back" aria-label="Zadní strana vizitky">
    <div class="wordmark"><span class="dot"></span>Klovarent</div>

    <div class="holder">
      <p class="name">Petr Hrubeš</p>
      <p>Lipová alej 2841/9</p>
      <p>Praha 5</p>
    </div>

    <div class="divider"></div>

    <ul class="contacts">
      <li>
        <svg viewBox="0 0 16 16" aria-hidden="true"><circle cx="8" cy="8" r="8" fill="#5a5a5e"/><path d="M5.4 4.2l1.3 0 .6 1.8-.8.6c.4.9 1 1.5 1.9 1.9l.6-.8 1.8.6 0 1.3c0 .4-.3.6-.7.6C7 10.1 5 8.1 4.8 4.9c0-.4.2-.7.6-.7z" fill="#fff"/></svg>
        +420 700 451 268
      </li>
      <li>
        <svg viewBox="0 0 16 16" aria-hidden="true"><circle cx="8" cy="8" r="8" fill="#5a5a5e"/><rect x="4" y="5.2" width="8" height="5.6" fill="none" stroke="#fff" stroke-width="1"/><path d="M4 5.4l4 3 4-3" fill="none" stroke="#fff" stroke-width="1"/></svg>
        petr.hrubes@klovarent-example.com
      </li>
      <li>
        <svg viewBox="0 0 16 16" aria-hidden="true"><circle cx="8" cy="8" r="8" fill="#5a5a5e"/><circle cx="8" cy="8" r="4" fill="none" stroke="#fff" stroke-width="1"/><ellipse cx="8" cy="8" rx="1.7" ry="4" fill="none" stroke="#fff" stroke-width=".9"/><path d="M4 8h8" stroke="#fff" stroke-width=".9"/></svg>
        www.klovarent-example.com
      </li>
    </ul>

    <div class="band">www.klovarent-example.com</div>
  </section>
</body>
</html>
```